Business card design, sleek & clean . For a notary loan signing business. I work with several lenders escrow officers etc . I am bilingual in Spanish , work 7 days a week to meet clients needs. Loan documents can be emailed for printing.

Not sure sleek clean logo

```html
<!DOCTYPE html>
<html lang="en">
<head>
<meta charset="utf-8">
<title>Marisol Vega – Notary Business Card</title>
<link rel="stylesheet" href="https://fonts.googleapis.com/css2?family=Cinzel:wght@400&family=Montserrat:wght@400;500&family=Open+Sans:wght@400&display=swap">
<style>
  :root {
    --backdrop: #f2f3f5;
    --navy: #1a1f4e;
    --gold: #dcb864;
    --white: #ffffff;
    --ink: #2a2a2a;
  }
  * { margin: 0; padding: 0; box-sizing: border-box; }
  html, body { width: 1200px; height: 962px; overflow: hidden; }
  body { background: var(--backdrop); position: relative; }

  .card { position: absolute; width: 539px; height: 318px; }
  .card--front { left: 331px; top: 129px; background: var(--navy); }
  .card--back { left: 338px; top: 506px; background: var(--white); }

  .brand-name {
    font-family: "Cinzel", serif;
    font-weight: 400;
    color: var(--gold);
    white-space: nowrap;
    letter-spacing: 0.01em;
  }
  .front-lockup {
    position: absolute; left: 0; right: 0; top: 140px; text-align: center;
  }
  .front-lockup .brand-name { font-size: 30px; line-height: 36px; }
  .front-lockup .tagline {
    margin-top: 8px;
    font-family: "Montserrat", sans-serif;
    font-weight: 500;
    font-size: 12px;
    letter-spacing: 0.42em;
    color: var(--white);
    padding-left: 0.42em;
  }

  .contact-list { position: absolute; left: 54px; top: 144px; list-style: none; }
  .contact-item {
    display: flex; align-items: center; gap: 6px;
    height: 21px;
    font-family: "Open Sans", sans-serif;
    font-size: 11.5px;
    color: var(--gold);
  }
  .contact-item svg { width: 14px; height: 14px; flex: none; }

  .social-row { position: absolute; left: 54px; top: 262px; display: flex; gap: 4px; }
  .social-dot { width: 15px; height: 15px; border-radius: 50%; background: var(--gold); }

  .divider {
    position: absolute; left: 268px; top: 54px; width: 2px; height: 208px;
    background: linear-gradient(to bottom, rgba(220,184,100,0), var(--gold) 20%, var(--gold) 80%, rgba(220,184,100,0));
  }

  .back-lockup { position: absolute; left: 320px; top: 188px; }
  .back-lockup .brand-name { font-size: 15px; line-height: 18px; }
  .back-lockup .tagline {
    margin-top: 3px;
    font-family: "Montserrat", sans-serif;
    font-weight: 500;
    font-size: 6.4px;
    letter-spacing: 0.04em;
    color: var(--ink);
  }
</style>
</head>
<body>

<section class="card card--front" aria-label="Card front">
  <div class="front-lockup">
    <div class="brand-name">MARISOL VEGA</div>
    <div class="tagline">NOTARIES PUBLIC</div>
  </div>
</section>

<section class="card card--back" aria-label="Card back">
  <ul class="contact-list">
    <li class="contact-item">
      <svg viewBox="0 0 14 14" aria-hidden="true">
        <rect width="14" height="14" rx="2" fill="#dcb864"/>
        <path d="M4.2 3.2c.4-.3.9-.2 1.1.2l.8 1.4c.2.4.1.8-.2 1l-.5.4c.4.9 1.1 1.7 2 2.1l.4-.5c.3-.3.7-.4 1-.2l1.4.8c.4.2.5.7.2 1.1l-.6.8c-.4.5-1.1.6-1.7.3C6 9.6 4.3 7.9 3.3 5.7c-.3-.6-.1-1.3.3-1.7z" fill="#ffffff"/>
      </svg>
      <span>(555)014-0192</span>
    </li>
    <li class="contact-item">
      <svg viewBox="0 0 14 14" aria-hidden="true">
        <rect width="14" height="14" rx="2" fill="#dcb864"/>
        <rect x="3" y="4.2" width="8" height="5.8" rx="0.6" fill="#ffffff"/>
        <path d="M3.2 4.6 7 7.4l3.8-2.8" fill="none" stroke="#dcb864" stroke-width="0.9"/>
      </svg>
      <span>mvega_notary@example.com</span>
    </li>
  </ul>

  <div class="social-row" aria-label="Social media links">
    <span class="social-dot"></span>
    <span class="social-dot"></span>
    <span class="social-dot"></span>
    <span class="social-dot"></span>
  </div>

  <div class="divider"></div>

  <div class="back-lockup">
    <div class="brand-name">MARISOL VEGA</div>
    <div class="tagline">NOTARY SIGNING AGENT &amp; HABLO ESPANOL</div>
  </div>
</section>

</body>
</html>
```